www.tralvexhealth.com

We are a company that is in the business of extending the life of surgical equipment by repairing or refurbishing equipment to save hospitals, surgery centers and clinics money. We call ourselves Basset Medical Corporation. We are in need of a website that delivers the "feel" of what of we do everyday. A website that explains our services but at the same time has a touch that is different from the rest. Many companies repair but their websites may not "pull" customers to inquire, we need that punch. At this time we are not looking for e-commerce but would like the option of adding that in the future. We do sell new and used equipment, so we like to be able to highlight those manufacturers on our site. We would like the website to have enough layouts for pictures to describe what we repair.
Target Market(s)
Biomedical Technicians and Managers, Hospital Purchasing Departments, OR Managers, type of facilities that our customer exists in, hospitals, surgery centers, clinics, animal hospitals
Industry/Entity Type
E-Commerce
Requirements
Must have
- An easy to navigate website, modern looking.
Easy to modify with pictures and or additional web pages
The winning designer to be available for future modifications and changes
Website to be unique compared to our competition, which are numerous
Nice to have
- E-Commerce capability

```html
<!DOCTYPE html>
<html lang="en">
<head>
<meta charset="utf-8">
<title>Basset Medical Corporation</title>
<link href="https://fonts.googleapis.com/css2?family=Roboto:wght@400;500;700&display=swap" rel="stylesheet">
<style>
:root{
  --green:#1ddc8c;
  --dark:#454545;
  --darker:#3a3a3a;
  --text:#444;
  --muted:#777;
  --line:#e2e2e2;
  --page:#f3f3f3;
  --panel:#fff;
}
*{box-sizing:border-box;margin:0;padding:0}
html,body{width:843px;height:1200px;overflow:hidden}
body{background:var(--page);font-family:"Roboto",Arial,sans-serif;color:var(--text);position:relative}
.abs{position:absolute}
.header{left:0;top:0;width:843px;height:140px;background:#fafafa}
.brand{left:30px;top:18px;font-size:27px;line-height:31px;font-weight:700;color:#3d3d3d;letter-spacing:.3px}
.topbar{right:30px;top:15px;font-size:9px;color:var(--muted);display:flex;align-items:center;gap:6px}
.currency{width:55px;height:15px;border:1px solid #ccc;background:#fff;font-size:8px;padding:1px 4px;color:#666;position:relative}
.currency:after{content:"";position:absolute;right:4px;top:5px;border:3px solid transparent;border-top-color:#888}
.langs{margin-left:10px;font-size:11px;font-weight:700;color:#666;display:flex;gap:7px}
.langs .on{color:var(--green)}
.account{left:580px;top:44px;width:87px;text-align:right;font-size:8.5px;color:var(--muted);line-height:12px}
.account b{color:#444;font-weight:500;font-size:9px}
.cart{left:676px;top:40px;width:130px;height:30px;background:var(--green);color:#fff;font-size:9px;display:flex;align-items:center;padding-left:8px;gap:8px}
.nav{left:18px;top:94px;width:804px;height:36px;background:var(--dark);display:flex;align-items:center}
.nav a{color:#fff;text-decoration:none;font-size:10.5px;font-weight:500;letter-spacing:.4px;height:36px;display:flex;align-items:center;padding:0 16px;border-right:1px solid #5a5a5a}
.nav .home{width:38px;justify-content:center;padding:0}
.search{left:596px;top:100px;width:164px;height:25px;background:#fff;display:flex;align-items:center;padding-left:4px;gap:8px;font-size:8.5px;color:#666}
.search-btn{left:760px;top:100px;width:56px;height:25px;background:var(--green);color:#fff;font-size:11px;display:flex;align-items:center;justify-content:center}
.panel{background:var(--panel);box-shadow:0 1px 2px rgba(0,0,0,.08)}
.cat-head{left:18px;top:154px;width:140px;height:30px;background:var(--green);color:#fff;font-size:11px;font-weight:700;padding:10px 9px;letter-spacing:.2px}
.cat-list{left:18px;top:188px;width:140px;list-style:none}
.cat-list li{height:22.6px;border-bottom:1px solid var(--line);font-size:10px;color:#555;padding:5px 7px}
.spec-head{left:18px;top:462px;width:140px;height:30px;background:var(--dark);color:#fff;font-size:9.5px;font-weight:500;padding:10px 10px;letter-spacing:.3px}
.special{left:18px;width:140px}
.special .ph{width:110px;height:100px;margin:0 auto 0 15px}
.special .name{color:var(--green);font-size:9px;font-weight:500;margin-top:10px}
.special .price{font-size:11.5px;margin-top:7px;color:#444}
.special .price s{font-size:7.5px;color:#777;margin-left:8px}
.special hr{border:0;border-top:1px solid var(--line);margin-top:12px}
.ph{border-radius:6px}
.hero-img{left:182px;top:154px;width:406px;height:344px;background:linear-gradient(135deg,#f4f4f4,#dcdcdc 60%,#bfbcbb)}
.hero-cap{left:182px;top:423px;width:406px;height:60px;background:rgba(255,255,255,.88);padding:14px 16px}
.hero-cap h2{font-size:17px;font-weight:400;color:#444}
.hero-cap h2 span{color:var(--green)}
.hero-cap p{font-size:7.5px;color:#666;margin-top:3px}
.hero-bar{left:182px;top:483px;width:406px;height:15px;background:#555;display:flex;justify-content:flex-end;align-items:center;gap:4px;padding-right:5px}
.dot{width:6px;height:6px;border-radius:50%;background:#aaa}
.dot.on{background:#fff}
.promo{left:596px;width:224px;height:109px;display:flex}
.promo .copy{width:110px;background:var(--dark);color:#fff;padding:16px 15px}
.promo h3{font-size:11px;font-weight:700;line-height:14px}
.promo p{font-size:7.5px;color:#bbb;line-height:10px;margin-top:2px}
.promo .btn{display:inline-block;background:var(--green);color:#fff;font-size:8px;font-weight:500;padding:4px 4px;margin-top:9px}
.promo .pimg{flex:1;background:linear-gradient(135deg,#f6f6f6,#e3e3e3)}
.sect{left:174px;width:656px;height:288px}
.sect h2{position:absolute;left:16px;top:14px;font-size:12.5px;font-weight:500;color:#444;letter-spacing:.2px}
.sect .rule{position:absolute;left:8px;top:38px;width:640px;height:1px;background:#ddd}
.grid{position:absolute;left:8px;top:48px;width:640px;display:flex}
.item{width:165px;height:224px;padding:14px 8px 0;border-left:1px solid var(--line)}
.item:first-child{border-left:0}
.item .ph{width:130px;height:126px;margin:0 auto}
.item .name{color:var(--green);font-size:8.5px;font-weight:500;margin-top:25px}
.item .price{font-size:11.5px;margin-top:10px}
.item .acts{display:flex;gap:2px;margin-top:10px}
.add{background:var(--green);color:#fff;font-size:8px;padding:5px 8px}
.view{background:var(--dark);color:#fff;font-size:8px;padding:5px 10px}
.features{left:10px;top:1108px;width:820px;height:68px;display:flex;align-items:center}
.feat{flex:1;height:40px;display:flex;align-items:center;justify-content:center;gap:12px;border-left:1px solid var(--line)}
.feat:first-child{border-left:0}
.feat b{display:block;color:var(--green);font-size:13.5px;font-weight:500}
.feat span{font-size:12.5px;color:#555}
.foot{right:14px;top:1186px;font-size:8px;color:#666}
</style>
</head>
<body>
<div class="abs header"></div>
<div class="abs brand">BASSET MEDICAL<br>CORPORATION</div>
<div class="abs topbar">Currency: <div class="currency">Dollar</div><div class="langs"><span class="on">EN</span><span>ES</span><span>FR</span></div></div>
<div class="abs account">Welcome ( <b>Log in</b> )<br><b>Your Account</b></div>
<div class="abs cart">
  <svg width="22" height="18" viewBox="0 0 22 18" fill="none" stroke="#fff" stroke-width="2"><path d="M1 2h4l3 10h10l2-7H7"/><circle cx="9" cy="15.5" r="1.3" fill="#fff"/><circle cx="17" cy="15.5" r="1.3" fill="#fff"/></svg>
  Cart: (empty)
</div>

<nav class="abs nav">
  <a class="home" href="#" aria-label="Home"><svg width="14" height="13" viewBox="0 0 14 13" fill="#fff"><path d="M7 0 0 6h2v7h4V9h2v4h4V6h2z"/></svg></a>
  <a href="#">ABOUT US</a><a href="#">NEW EQUIPMETNS</a><a href="#">USED EQUIPMETNS</a><a href="#">DELIVERY</a><a href="#">CONTACT</a>
</nav>
<div class="abs search"><svg width="18" height="18" viewBox="0 0 18 18" fill="none" stroke="#ccc" stroke-width="1.5"><circle cx="9" cy="9" r="7.5"/></svg>Search</div>
<div class="abs search-btn">Search</div>

<div class="abs panel" style="left:10px;top:146px;width:156px;height:300px"></div>
<div class="abs cat-head">CATEGORIES</div>
<ul class="abs cat-list">
  <li>Baby &amp; Child Care</li><li>Medicine Cabinet</li><li>Surgical Camera</li><li>Endoscope Repair</li><li>Surgical Power</li><li>Surgical Camera</li><li>Endoscope Repair</li><li>Surgical Power</li><li>Surgical &nbsp;Repair</li><li>Surgical Power</li><li style="border:0">Surgical Camera</li>
</ul>

<div class="abs panel" style="left:10px;top:454px;width:156px;height:584px"></div>
<div class="abs spec-head">SPECIALS</div>
<div class="abs special" style="top:506px">
  <div class="ph" role="img" aria-label="Handheld blood testing meters" style="background:linear-gradient(135deg,#dbe9f3,#9bbcd6)"></div>
  <div class="name">Veltrona XS System</div>
  <div class="price">$28.93 <s>$32.00</s></div><hr>
</div>
<div class="abs special" style="top:686px">
  <div class="ph" role="img" aria-label="Surgical power drill" style="background:linear-gradient(135deg,#eee,#9a9a9a)"></div>
  <div class="name">Vortan 3ti</div>
  <div class="price">$26.06 <s>$28.00</s></div><hr>
</div>
<div class="abs special" style="top:866px">
  <div class="ph" role="img" aria-label="Blue medical face mask" style="background:linear-gradient(135deg,#e8f3fa,#a9d1ea)"></div>
  <div class="name">Aeris Medical face mask</div>
  <div class="price">$26.06 <s>$28.00</s></div>
</div>

<div class="abs panel" style="left:174px;top:146px;width:656px;height:360px"></div>
<div class="abs hero-img" role="img" aria-label="Robotic surgical system with monitors"></div>
<div class="abs hero-cap"><h2><span>REPAIRING</span> Surgical Equipments</h2><p>Excepteur sint occaecat cupidatat non proident, sunt in culpa qui officia &nbsp;<span style="color:var(--green)">▸</span></p></div>
<div class="abs hero-bar"><i class="dot"></i><i class="dot on"></i><i class="dot"></i></div>

<div class="abs promo" style="top:154px"><div class="copy"><h3>LOREM IPSUM DOLOR SIT</h3><p>Lorem ipsum dolor sit amet conse ctetur</p><span class="btn">Inquire Now</span></div><div class="pimg" role="img" aria-label="Portable patient monitor"></div></div>
<div class="abs promo" style="top:271px"><div class="copy"><h3>EXCEPTEUR SINT</h3><p>Lorem ipsum dolor sit amet conse ctetur</p><span class="btn">Inquire Now</span></div><div class="pimg" role="img" aria-label="Vital signs monitor"></div></div>
<div class="abs promo" style="top:389px"><div class="copy"><h3>OCCAECAT CUPIDATAT</h3><p>Lorem ipsum dolor sit amet conse ctetur</p><span class="btn">Inquire Now</span></div><div class="pimg" role="img" aria-label="Medical scanning device"></div></div>

<section class="abs panel sect" style="top:514px">
  <h2>USED EQUIPMENTS</h2><div class="rule"></div>
  <div class="grid">
    <div class="item"><div class="ph" role="img" aria-label="Blue medical face mask" style="background:linear-gradient(135deg,#eef7fc,#a9d1ea)"></div><div class="name">Aeris Medical face mask</div><div class="price">$26.06</div><div class="acts"><span class="add">Add to cart</span><span class="view">View</span></div></div>
    <div class="item"><div class="ph" role="img" aria-label="Surgical power drill" style="background:linear-gradient(135deg,#f0f0f0,#9a9a9a)"></div><div class="name">Vortan 3ti</div><div class="price">$26.06</div><div class="acts"><span class="add">Add to cart</span><span class="view">View</span></div></div>
    <div class="item"><div class="ph" role="img" aria-label="Handheld analyser with test strips" style="background:linear-gradient(135deg,#f7f4ee,#f2a63a)"></div><div class="name">Lumetrix Plus System</div><div class="price">$28.96</div><div class="acts"><span class="add">Add to cart</span><span class="view">View</span></div></div>
    <div class="item"><div class="ph" role="img" aria-label="Laboratory staining instrument" style="background:linear-gradient(135deg,#eef1f5,#5d6c84)"></div><div class="name">Stainline XT</div><div class="price">$28.96</div><div class="acts"><span class="add">Add to cart</span><span class="view">View</span></div></div>
  </div>
</section>

<section class="abs panel sect" style="top:810px">
  <h2>NEW EQUIPMENTS</h2><div class="rule"></div>
  <div class="grid">
    <div class="item"><div class="ph" role="img" aria-label="Blue medical face mask" style="background:linear-gradient(135deg,#eef7fc,#a9d1ea)"></div><div class="name">Aeris Medical face mask</div><div class="price">$26.06</div><div class="acts"><span class="add">Add to cart</span><span class="view">View</span></div></div>
    <div class="item"><div class="ph" role="img" aria-label="Surgical power drill" style="background:linear-gradient(135deg,#f0f0f0,#9a9a9a)"></div><div class="name">Vortan 3ti</div><div class="price">$26.06</div><div class="acts"><span class="add">Add to cart</span><span class="view">View</span></div></div>
    <div class="item"><div class="ph" role="img" aria-label="Handheld analyser with test strips" style="background:linear-gradient(135deg,#f7f4ee,#f2a63a)"></div><div class="name">Lumetrix Plus System</div><div class="price">$28.96</div><div class="acts"><span class="add">Add to cart</span><span class="view">View</span></div></div>
    <div class="item"><div class="ph" role="img" aria-label="Laboratory staining instrument" style="background:linear-gradient(135deg,#eef1f5,#5d6c84)"></div><div class="name">Stainline XT</div><div class="price">$28.96</div><div class="acts"><span class="add">Add to cart</span><span class="view">View</span></div></div>
  </div>
</section>

<div class="abs panel features">
  <div class="feat"><svg width="52" height="34" viewBox="0 0 52 34" fill="none" stroke="#ccc" stroke-width="5"><path d="M8 16a10 10 0 0 1 10-10h24M36 1l6 5-6 5M44 18a10 10 0 0 1-10 10H10M16 23l-6 5 6 5"/></svg><div><b>30-Day</b><span>Easy return</span></div></div>
  <div class="feat"><svg width="34" height="40" viewBox="0 0 34 40" fill="#ccc"><path d="M8 18v-6a9 9 0 0 1 18 0v6h-4v-6a5 5 0 0 0-10 0v6z"/><rect x="3" y="18" width="28" height="21" rx="2"/></svg><div><b>Secure</b><span>Shopping</span></div></div>
  <div class="feat"><svg width="38" height="40" viewBox="0 0 38 40" fill="#ccc"><rect x="1" y="17" width="8" height="22"/><path d="M12 18l7-10 2-7c4 0 6 3 5 8l-2 6h11c2 0 3 2 2 4l-4 17c0 2-2 3-4 3H12z"/></svg><div><b>Satisfaction</b><span>100% Guaranteed</span></div></div>
  <div class="feat"><svg width="40" height="40" viewBox="0 0 40 40" fill="none" stroke="#ccc"><circle cx="20" cy="20" r="18" stroke-width="3"/><circle cx="20" cy="20" r="13" stroke-width="2"/><text x="20" y="27" text-anchor="middle" font-size="18" font-family="Roboto,Arial,sans-serif" fill="#ccc" stroke="none" font-weight="700">$</text></svg><div><b>Lowest Prices</b><span>Guaranteed</span></div></div>
</div>
<div class="abs foot">© 2013 Basset Medical Corporation. All rights reserved</div>
</body>
</html>
```